Flyer-Design für Achtsamkeitscoaching
Zielgruppe
-Achtsamkeitscoaching - Stressbewältigung - Persönlichkeitsstärkung - Burnout Bewältigung
Aufgabenstellung
Faltflyer, 21 x 21cm, Titelseite: oberes Viertel soll 'härter' wirken - > anschließend in weichere Formen und Farbe übergehend, Grundfarbe = Pastell blaugrün, Logo + Akzente = Gold oder orange

```html
<!DOCTYPE html>
<html lang="de">
<head>
<meta charset="utf-8">
<title>Achtsamkeits-Coaching Faltflyer</title>
<link href="https://fonts.googleapis.com/css2?family=Kaushan+Script&family=Montserrat:wght@300;400;600;700&family=Permanent+Marker&display=swap" rel="stylesheet">
<style>
:root{
  --green:#8cc02a;
  --green-light:#b8d65c;
  --cream:#eef3d6;
  --gold:#d4913a;
  --white:#ffffff;
  --soft:#e6f0c4;
  --bg:#b9b9b9;
  --script:"Kaushan Script", cursive;
  --marker:"Permanent Marker", "Kaushan Script", cursive;
  --sans:"Montserrat", sans-serif;
}
*{box-sizing:border-box;margin:0;padding:0}
html,body{width:1200px;height:800px;overflow:hidden;background:var(--bg)}
.canvas{position:relative;width:1200px;height:800px}
.spread{position:absolute;top:40px;width:560px;height:720px;display:flex;box-shadow:0 6px 18px rgba(0,0,0,.25)}
.spread--outside{left:20px}
.spread--inside{left:620px}
.panel{position:relative;width:280px;height:720px;overflow:hidden;background:var(--green);color:var(--white);font-family:var(--sans)}
.panel-bg{position:absolute;inset:0;width:100%;height:100%}
.panel-content{position:absolute;inset:0}

/* cover */
.cover-questions{position:absolute;left:40px;top:50px;font-family:var(--marker);font-weight:400;font-size:24px;line-height:1.15;color:var(--white);transform:rotate(-8deg)}
.cover-questions span{display:block}
.cover-questions span:nth-child(2){margin-left:14px}
.cover-questions span:nth-child(3){margin-left:28px;letter-spacing:3px}
.cover-headline{position:absolute;left:28px;top:250px;font-family:var(--script);font-size:38px;color:var(--gold);transform:rotate(-10deg)}
.cover-brand{position:absolute;left:0;right:0;top:370px;display:flex;align-items:center;justify-content:center;gap:10px;font-weight:600;font-size:18px;color:var(--gold)}
.cover-brand .dot{width:16px;height:16px;border-radius:50%;background:var(--gold)}
.cover-footer{position:absolute;left:20px;right:12px;top:528px}
.cover-title{font-weight:700;font-size:16px;letter-spacing:.2px;white-space:nowrap}
.cover-name{font-weight:300;font-size:18px;color:var(--soft);margin:2px 0 10px 36px}
.cover-values{font-weight:700;font-size:12.5px;line-height:1.35;margin-left:36px}
.cover-cert{font-weight:300;font-size:10.5px;line-height:1.4;color:var(--soft);margin-top:12px;white-space:nowrap}

/* krafttier */
.intro-text{position:absolute;left:22px;right:20px;top:30px;font-size:9.5px;line-height:1.45}
.intro-text p+p{margin-top:6px}
.totem-title{position:absolute;left:120px;top:205px;font-family:var(--script);font-size:30px;line-height:1.05;color:var(--gold);transform:rotate(-8deg)}
.totem-title span{display:block;margin-left:30px}
.dragonfly-photo{position:absolute;left:24px;top:268px;width:160px;height:90px;border-radius:50% 40% 50% 40%;background:linear-gradient(135deg,#1d5d86,#2a8f9c 55%,#c9d7c8)}
.totem-tagline{position:absolute;right:22px;top:372px;text-align:right;color:var(--gold);font-size:14px;transform:rotate(-8deg)}
.totem-tagline strong{display:block;font-weight:400;letter-spacing:.5px}
.body-text{position:absolute;left:22px;right:20px;top:500px;font-size:10px;line-height:1.5}
.body-text p+p{margin-top:10px}

/* inside */
.section-script{position:absolute;font-family:var(--script);font-weight:400;color:var(--gold);line-height:1.1}
.fit-title{left:22px;top:26px;font-size:18px;transform:rotate(4deg)}
.list-heading{font-family:var(--script);font-weight:400;font-size:16px;margin:0 0 6px}
.fit-lists{position:absolute;left:22px;right:18px;top:108px;font-size:10px;line-height:1.35}
.fit-lists ul{list-style:none}
.fit-lists li{margin-bottom:7px;padding-left:10px;text-indent:-10px}
.fit-lists li::before{content:"- "}
.fit-lists .list-heading+ul{margin-bottom:12px}
.no-list{width:120px}
.portrait{position:absolute;right:0;bottom:22px;width:130px;height:200px;border-radius:64px 64px 0 0;background:linear-gradient(180deg,#6b3b22 0%,#a3643d 45%,#7fd1cf 100%)}
.mini-brand{position:absolute;left:22px;bottom:80px;font-weight:600;font-size:12px;color:var(--white);display:flex;align-items:center;gap:6px;white-space:nowrap}
.mini-brand .dot{width:10px;height:10px;border-radius:50%;background:var(--white)}

.benefits-title{left:26px;top:30px;font-size:19px;transform:rotate(-6deg)}
.benefits{position:absolute;left:22px;right:18px;top:112px;font-size:10px;line-height:1.35;list-style:none}
.benefits li{margin-bottom:8px;padding-left:10px;text-indent:-10px}
.benefits li::before{content:"- "}
.prejudice{position:absolute;left:22px;right:18px;top:470px;font-size:10px;line-height:1.5}
.prejudice h3{font-size:10.5px;font-weight:600;margin-bottom:4px}
.contact{position:absolute;right:30px;top:600px;text-align:center}
.contact h3{font-family:var(--script);font-weight:400;font-size:22px}
.contact p{font-size:11px;margin-top:4px}
</style>
</head>
<body>
<div class="canvas">

  <div class="spread spread--outside">
    <section class="panel panel--cover">
      <svg class="panel-bg" viewBox="0 0 280 720" preserveAspectRatio="none" aria-hidden="true">
        <rect width="280" height="720" fill="var(--green)"/>
        <path d="M0 215 Q140 150 280 150 L280 470 Q150 520 0 520 Z" fill="var(--cream)"/>
        <path d="M0 215 Q140 150 280 150" fill="none" stroke="var(--gold)" stroke-width="4"/>
        <path d="M280 470 Q150 520 0 520" fill="none" stroke="var(--gold)" stroke-width="4"/>
      </svg>
      <div class="panel-content">
        <h2 class="cover-questions"><span>Gestresst?</span><span>Erschöpft?</span><span>Genervt?</span></h2>
        <p class="cover-headline">Ich helfe Dir!</p>
        <div class="cover-brand"><span class="dot"></span>Lena Hartwig</div>
        <div class="cover-footer">
          <h1 class="cover-title">ACHTSAMKEITS-COACHING</h1>
          <p class="cover-name">mit Lena Hartwig</p>
          <p class="cover-values">kompetent und erfahren<br>ganzheitlich und flexibel<br>persönlich und vertraulich</p>
          <p class="cover-cert">Zertifizierte Achtsamkeitstrainerin und<br>IHK-geprüfte Stressmanagerin</p>
        </div>
      </div>
    </section>

    <section class="panel panel--totem">
      <svg class="panel-bg" viewBox="0 0 280 720" preserveAspectRatio="none" aria-hidden="true">
        <rect width="280" height="720" fill="var(--green-light)"/>
        <path d="M0 190 Q140 150 280 110 L280 400 Q160 470 0 460 Z" fill="var(--cream)"/>
        <path d="M0 190 Q140 150 280 110" fill="none" stroke="var(--gold)" stroke-width="4"/>
        <path d="M280 400 Q160 470 0 460" fill="none" stroke="var(--gold)" stroke-width="4"/>
        <path d="M0 460 Q160 470 280 400 L280 720 L0 720 Z" fill="var(--green)"/>
      </svg>
      <div class="panel-content">
        <div class="intro-text">
          <p>In einem kurzen Vorgespräch schauen wir in Deine Lebensbereiche, damit du einen IST-Stand für Dich erkennen kannst, an welchem du am Anfang Deiner Veränderung startest.</p>
          <p>Die Libelle fliegt in Dein Leben und bringt Dir Mut, Liebe und Zuversicht. Sie begleitet Dich.</p>
        </div>
        <p class="totem-title">Krafttier<span>Libelle:</span></p>
        <div class="dragonfly-photo" role="img" aria-label="Foto einer blau schimmernden Libelle"></div>
        <p class="totem-tagline"><strong>ERLAUBNIS</strong>zum Richtungswechsel</p>
        <div class="body-text">
          <p>Gehe langsam, achtsam und bewusst Deine nächsten Schritte. Dein Leben richtet sich neu aus. Gehe mit, lasse das Alte los und erlaube Dir einen Richtungswechsel. Nimm Dein Leben in die Hand und schaffe Platz für Neues. Jetzt bist du bereit. Innerlich weißt du schon, in welchen Bereichen Du einen wirklichen Richtungswechsel brauchst.</p>
          <p>Höre Dir selbst zu, so bewältigst Du ganz leicht die Hürden, die auf Deinem Weg auf Dich warten.</p>
        </div>
      </div>
    </section>
  </div>

  <div class="spread spread--inside">
    <section class="panel panel--fit">
      <svg class="panel-bg" viewBox="0 0 280 720" preserveAspectRatio="none" aria-hidden="true">
        <rect width="280" height="720" fill="var(--cream)"/>
        <path d="M0 75 Q140 80 280 100 L280 690 Q140 686 0 680 Z" fill="var(--green)"/>
        <path d="M40 130 L180 135" stroke="var(--cream)" stroke-width="1.5"/>
      </svg>
      <div class="panel-content">
        <h2 class="section-script fit-title">Ist mein Achtsamkeitscoaching<br>für dich geeignet?</h2>
        <div class="fit-lists">
          <h3 class="list-heading">Yes! Wenn Du –</h3>
          <ul>
            <li>raus willst, aus Deinem privaten und/ oder beruflichen Stress-Hamsterrad</li>
            <li>Dich müde, gereizt, verspannt, unruhig, wenig belastbar, unkonzentriert fühlst</li>
            <li>das Gefühl hast, in dieser schnelllebigen Zeit kurz zu kommen</li>
            <li>Dinge nicht nur verstehen, sondern auch umsetzen willst</li>
            <li>nach Selbstvertrauen, Klarheit und innerer Ruhe strebst und bereit bist deine Komfortzone dafür zu verlassen</li>
            <li>wieder Du selbst werden möchtest und Dich wieder fühlen willst!</li>
          </ul>
          <h3 class="list-heading">No! Wenn Du –</h3>
          <ul class="no-list">
            <li>nur einen kurzen Motivationskick suchst und nicht bereit bist Deine Verhaltensmuster zu hinterfragen</li>
            <li>keine Zeit und kein Geld investieren willst</li>
          </ul>
        </div>
        <div class="mini-brand"><span class="dot"></span>Lena Hartwig</div>
        <div class="portrait" role="img" aria-label="Porträtfoto der Coachin"></div>
      </div>
    </section>

    <section class="panel panel--benefits">
      <svg class="panel-bg" viewBox="0 0 280 720" preserveAspectRatio="none" aria-hidden="true">
        <rect width="280" height="720" fill="var(--cream)"/>
        <path d="M0 100 Q140 84 280 78 L280 680 Q140 676 0 690 Z" fill="var(--green)"/>
        <path d="M150 90 L270 86" stroke="var(--green)" stroke-width="3"/>
      </svg>
      <div class="panel-content">
        <h2 class="section-script benefits-title">Vorteile<br>Deines Coachings!</h2>
        <ul class="benefits">
          <li>Du wirst individuell und persönlich betreut.</li>
          <li>Herzlich und offen – ich begleite Dich, ohne Dich zu bewerten</li>
          <li>Schneller Einstieg möglich. Keine Vorkenntnisse notwendig.</li>
          <li>Ganzheitlich – Ich bringe Dich nicht nur auf den Weg in die Achtsamkeit, sondern betrachte Deine Symptome auch in größeren Zusammenhängen</li>
          <li>Planbar – das Coaching findet einmal pro Woche im Zeitraum von acht Wochen statt – Nimm Dir die Zeit!</li>
          <li>Zielgruppe ALLE! – mein Coaching ist für dich geeignet, wenn Du dir sagst „Ich will es – jetzt!“</li>
          <li>Das besondere Geschenk für Deine (n) Partnerin/ Partner, und die Krönung ist, wenn ihr es gemeinsam angeht. Liebe beruht auf Gegenseitigkeit.</li>
          <li>Ideal für Paare – es kann nur noch besser werden</li>
        </ul>
        <div class="prejudice">
          <h3>Ein Wort zu Vorurteilen:</h3>
          <p>Nein, es sind keine Hokuspokus-Stunden oder spirituelle Beweihräucherungen. Die Lehre der Achtsamkeit beruht auf langjährig erprobten und wissenschaftlich fundamentierten Erkenntnissen und ist längst in der modernen Arbeitswelt fest integriert.</p>
        </div>
        <div class="contact">
          <h3>Kontakt</h3>
          <p>Adresse</p>
        </div>
      </div>
    </section>
  </div>

</div>
</body>
</html>
```